Business card design based on existing website

Please make a business card that is consistent with the look and feel of my new website: http://brindleworth.com.sg. By going to the site, I think you'll have all you need in terms of the work I do and the colors I use.

I would like to ask the winner of this project to then do a separate project to design my stationery.

Target Market(s)

Heads of human resources, people wanting psychotherapy, and executives wanting coaching. (It's quite a mix!)

Industry/Entity Type

Psychology

Contact Information for Business Card

Email: pax5678@brindleworth.com.sg
Website: http://brindleworth.com.sg
Tel: +65 94706152

(I will not have a physical address on the card)

Font styles to use
Serif

Colors

Designer to choose colors to be used in the design.

Requirements
Must have
• On the Front
• ==========
• Have "Dr. Everett Brindleworth" using the font of the website.
• Also "Executive Coach, Psychotherapist, Leadership Professor"
• The back should mention
• ==================
• My degrees
• -------------
• "PhD Kelvale; Post Doc Duncliffe". E.g., "Everett Brindleworth (PhD Kelvale; Post Doc Duncliffe)" where the text between brackets was in smaller font.
• My work
• ----------
• "Executive coach, psychotherapist, and leadership professor"
• My job titles
• ---------------
• "Principal (Brindleworth Consulting)
• Adjunct Professor (Orchid Crest University)
• Adjunct Associate Professor (Meridian Strait University)
• Coach & Supervisor (VORELT) '
• Options:
• 1) you can abbreviate Adjunct Professor to "Adj Prof" or "Adj Professor"; and "Adjunct Associate Professor" to "Adj Assoc Prof"
• 2) you abbreviate "Meridian Strait University" and "Orchid Crest University" to "MSU" and "OCU"
• 3) You can also combine the titles for MSU and OCU, e.g., "Adjunct faculty (MSU & OCU)
Nice to have
• Because I work with many Chinese people, it is sometimes helpful to have my family name, "Brindleworth", in caps. In the past I have not used caps because it takes away from the aesthetic of the card. Only use caps if it looks good.
• The uploaded image of a "EB" is something that may be helpful. I am undecided.
• THANK YOU for helping me!
Should not have
• No photos. In my industry people consider it overselling.

```html
<!DOCTYPE html>
<html lang="en">
<head>
<meta charset="utf-8">
<title>Everett Brindleworth – Business Card</title>
<link rel="stylesheet" href="https://fonts.googleapis.com/css2?family=Marcellus&family=PT+Sans&family=EB+Garamond:wght@500;600&display=swap">
<style>
  :root {
    --page: #ffffff;
    --card-green: #15302a;
    --card-green-back: #132d27;
    --accent-stone: #9c9c88;
    --ink-cream: #ece8d6;
    --ink-gold: #e6dec0;
    --front-edge: #c8c8c8;
    --back-edge: #1a1a1a;
  }
  * { margin: 0; padding: 0; box-sizing: border-box; }
  html, body {
    width: 1200px;
    height: 384px;
    overflow: hidden;
    background: var(--page);
  }
  .canvas {
    position: relative;
    width: 1200px;
    height: 384px;
  }
  .card {
    position: absolute;
    top: 36px;
    width: 557px;
    height: 310px;
    overflow: hidden;
  }
  .card--front {
    left: 26px;
    background: var(--card-green);
    border: 1px solid var(--front-edge);
  }
  .card--back {
    left: 625px;
    background: var(--card-green-back);
    border: 1px solid var(--back-edge);
  }
  .front-swoosh {
    position: absolute;
    left: 0;
    top: 0;
    width: 557px;
    height: 310px;
  }
  .front-name {
    position: absolute;
    top: 52px;
    left: 0;
    width: 100%;
    text-align: center;
    font-family: "Marcellus", serif;
    font-size: 36px;
    color: var(--ink-cream);
    letter-spacing: 0.2px;
  }
  .front-roles {
    position: absolute;
    top: 103px;
    left: 0;
    width: 100%;
    display: flex;
    justify-content: center;
    gap: 20px;
    font-family: "PT Sans", sans-serif;
    font-size: 12.5px;
    color: var(--ink-cream);
  }
  .front-titles {
    position: absolute;
    top: 164px;
    left: 0;
    width: 100%;
    text-align: center;
    list-style: none;
    font-family: "PT Sans", sans-serif;
    font-size: 14.5px;
    line-height: 18px;
    color: var(--ink-cream);
  }
  .back-name {
    position: absolute;
    top: 36px;
    left: 60px;
    width: 210px;
    text-align: center;
    font-family: "EB Garamond", serif;
    font-weight: 500;
    font-size: 22px;
    color: var(--ink-gold);
  }
  .back-degrees {
    position: absolute;
    top: 72px;
    left: 54px;
    font-family: "EB Garamond", serif;
    font-weight: 600;
    font-size: 14px;
    color: var(--ink-gold);
  }
  .back-contact {
    position: absolute;
    top: 218px;
    left: 266px;
    width: 260px;
    text-align: center;
    list-style: none;
    font-family: "EB Garamond", serif;
    font-weight: 600;
    font-size: 13.5px;
    line-height: 19px;
    color: var(--ink-gold);
  }
</style>
</head>
<body>
<main class="canvas">
  <section class="card card--front" aria-label="Card front">
    <svg class="front-swoosh" viewBox="0 0 557 310" aria-hidden="true">
      <path d="M360 310 Q 470 282 557 218 L557 310 Z" fill="var(--accent-stone)"/>
    </svg>
    <h1 class="front-name">Dr. Everett Brindleworth</h1>
    <p class="front-roles">
      <span>Executive Coach</span>
      <span>Psychotherapist</span>
      <span>Leadership Professor</span>
    </p>
    <ul class="front-titles">
      <li>Principal (Brindleworth Consulting)</li>
      <li>Adj. Professor (OCU)</li>
      <li>Adj. Assoc. Professor (MSU)</li>
      <li>Coach &amp; Supervisor (VORELT)</li>
    </ul>
  </section>

  <section class="card card--back" aria-label="Card back">
    <h2 class="back-name">Everett Brindleworth</h2>
    <p class="back-degrees">(PhD Kelvale; Post Doc Duncliffe)</p>
    <ul class="back-contact">
      <li>Tel: +65 94706152</li>
      <li>Email: pax5678@brindleworth.com.sg</li>
      <li>Website: http://brindleworth.com.sg</li>
    </ul>
  </section>
</main>
</body>
</html>
```